Roving Watchpost Hub Banner

A pull up banner for use at trade shows advertising our RWPH (Roving Watchpost Hub) featuring Harbor Lantern Systems cloud based CCTV system. The artwork should be suitable for a 850mm wide x 2000mm high pull up banner. The banner needs to feature our logo, the RWPH brand & the Harbor Lantern logo as well as a large picture of the RWPH. I'm going to send through a few of these so the designers can be creative. The solution is used for rapid deployment in the event of an incident or emergency- so the banner needs to reflect the serious nature of its function. Most of our marketing collateral is on a black background with a cityscape image at night (see website). I'd like the banner to keep this style.
The slogan "The Ultimate Rapid Deploy Surveillance Solution" should appear on the banner as should the website address: qorvanrwph.example.au

Target Market(s)

Governement and critical infrastructure agencies. Private security and law enforcement. Event management companies

Industry/Entity Type

Trade

Font styles to use
Sans Serif

Colors
c2e4f2
33a6d7
85cae6
85abd2
1b1b1b
000000

Requirements
Must have
• Large picture

```html
<!DOCTYPE html>
<html lang="en">
<head>
<meta charset="utf-8">
<title>Roving Watchpost Hub – Pull Up Banner</title>
<link rel="stylesheet" href="https://fonts.googleapis.com/css2?family=Bebas+Neue&display=swap">
<style>
  :root {
    --page-bg: #f2f3f5;
    --banner-blue: #2b4fae;
    --banner-deep: #1a3380;
    --banner-navy: #101c52;
    --sky-light: #c2e4f2;
    --sky-mid: #85cae6;
    --accent-blue: #33a6d7;
    --steel-blue: #85abd2;
    --ink: #1b1b1b;
    --white: #ffffff;
  }
  html, body {
    margin: 0;
    width: 1200px;
    height: 1064px;
    overflow: hidden;
    background: var(--page-bg);
  }
  .canvas {
    position: relative;
    width: 1200px;
    height: 1064px;
  }
  .banner {
    position: absolute;
    left: 425px;
    top: 32px;
    width: 350px;
    height: 1000px;
    overflow: hidden;
    background: var(--banner-blue);
    font-family: "Bebas Neue", "Arial Narrow", sans-serif;
  }
  .cityscape {
    position: absolute;
    inset: 0 0 140px 0;
    background:
      linear-gradient(90deg, rgba(16,28,82,0.35) 0%, rgba(16,28,82,0) 30%, rgba(16,28,82,0) 70%, rgba(16,28,82,0.3) 100%),
      linear-gradient(180deg, #2f52b2 0%, #2b4eae 35%, #2748a2 60%, #1e3a8c 85%, #1a3380 100%);
  }
  .footer-band {
    position: absolute;
    left: 0; right: 0; bottom: 0;
    height: 140px;
    background: var(--banner-navy);
  }
  .headline {
    position: absolute;
    left: 17px;
    top: 28px;
    margin: 0;
    color: var(--white);
    font-weight: 400;
    font-size: 68px;
    line-height: 77px;
    letter-spacing: 0.5px;
    text-transform: uppercase;
  }
  .headline span { display: block; }
  .web-address {
    position: absolute;
    left: 19px;
    top: 518px;
    padding: 2px 8px 0;
    height: 32px;
    line-height: 32px;
    background: var(--white);
    color: var(--banner-deep);
    font-size: 24px;
    letter-spacing: 0.5px;
  }
  .photo {
    position: absolute;
    border: 2px solid var(--white);
    box-sizing: border-box;
  }
  .photo-frame {
    position: absolute;
    border: 2px solid rgba(255,255,255,0.85);
    box-sizing: border-box;
  }
  .photo-mast-tall {
    left: 79px; top: 713px; width: 107px; height: 183px;
    background: linear-gradient(180deg, #5e95d8 0%, #8fbbe9 45%, #b6d3ef 70%, #3d4a3a 85%, #1f2430 100%);
  }
  .frame-mast-tall { left: 73px; top: 707px; width: 119px; height: 195px; }
  .photo-van-side {
    left: 211px; top: 640px; width: 130px; height: 240px;
    background: linear-gradient(180deg, #dbe7f3 0%, #c4d8ec 40%, #8d98a6 55%, #2a2d33 68%, #3b3e44 88%, #6d6f72 100%);
  }
  .frame-van-side { left: 205px; top: 634px; width: 142px; height: 252px; }
  .photo-van-front {
    left: 186px; top: 868px; width: 128px; height: 122px;
    background: linear-gradient(180deg, #bdb9b3 0%, #a5a19b 40%, #1d1f24 62%, #23252a 82%, #8e8b86 100%);
  }
  .frame-van-front { left: 180px; top: 862px; width: 140px; height: 132px; }
  .brand-panel {
    position: absolute;
    left: 9px;
    top: 888px;
    width: 164px;
    height: 102px;
    background: var(--white);
  }
  .brand-panel .stripe {
    position: absolute;
    left: 0; right: 0;
    height: 12px;
    background: var(--sky-mid);
  }
  .brand-panel .stripe.top { top: 0; }
  .brand-panel .stripe.bottom { bottom: 0; }
  .brand-row {
    position: absolute;
    top: 38px;
    left: 0; right: 0;
    display: flex;
    justify-content: space-around;
    align-items: center;
    color: var(--accent-blue);
    font-size: 17px;
    line-height: 1;
  }
  .brand {
    display: flex;
    align-items: center;
    gap: 4px;
  }
  .brand-dot {
    width: 12px; height: 12px;
    border-radius: 50%;
    background: var(--accent-blue);
  }
  .brand-square {
    width: 10px; height: 10px;
    background: var(--accent-blue);
  }
</style>
</head>
<body>
  <main class="canvas">
    <section class="banner">
      <div class="cityscape" role="img" aria-label="Night cityscape of office towers in deep blue tones"></div>
      <div class="footer-band"></div>

      <h1 class="headline">
        <span>The</span>
        <span>Ultimate</span>
        <span>Rapid</span>
        <span>Deploy</span>
        <span>Surveillance</span>
        <span>Solution</span>
      </h1>

      <div class="web-address">qorvanrwph.example.au</div>

      <div class="photo-frame frame-mast-tall"></div>
      <div class="photo photo-mast-tall" role="img" aria-label="Roving Watchpost Hub van with extended camera mast under a blue sky"></div>

      <div class="photo-frame frame-van-side"></div>
      <div class="photo photo-van-side" role="img" aria-label="Side view of the black Roving Watchpost Hub van with raised mast"></div>

      <div class="brand-panel">
        <div class="stripe top"></div>
        <div class="brand-row">
          <span class="brand"><span class="brand-dot"></span>RWPH</span>
          <span class="brand"><span class="brand-square"></span>Harbor Lantern</span>
        </div>
        <div class="stripe bottom"></div>
      </div>

      <div class="photo-frame frame-van-front"></div>
      <div class="photo photo-van-front" role="img" aria-label="Roving Watchpost Hub van parked indoors with roof camera"></div>
    </section>
  </main>
</body>
</html>
```